Power Washing Business Easy Postcard Design

We need a postcard designed for our company, which does residential power washing. We clean houses, decks, driveways and fences. The design should be understated, high end with minimalist graphics. No bubbles or wild colors. The name of the business is "stoneridge power washing" which should be rendered all lower case in a san serif font. Sample files in blue or white are attached. The attached files aren't our logo, just a model. The font doesn't have to be exact and "power washing" needs to be added to it.The postcard size is the Marlo Press 8.64" X 5.59". The photo which is attached should fill the whole front of the card.

The text elements on the front are:
1) "stoneridge power washing"- as per the attached files, can be broken into two lines

2) "Mention this card and receive a FREE standard size Deck Wash"

3) "804-555-3186"

4) "stoneridgepowerwashing.example" (this font size can be smaller than the phone number.)

5)"We Clean:- Houses- Decks- Driveways- Fences"The arrangement is the text is up to you. The text should not overpower the image.

Target Market(s)

Homeowners

Industry/Entity Type

Residential

Font styles to use
Sans Serif

Requirements
Should not have
• Garish graphics

```html
<!DOCTYPE html>
<html lang="en">
<head>
<meta charset="utf-8">
<title>stoneridge power washing – postcard</title>
<link rel="stylesheet" href="https://fonts.googleapis.com/css2?family=Questrial&display=swap">
<style>
  :root {
    --navy: #1d3f8c;
    --band-blue: #1f4f9e;
    --sky-blue: #74cdf3;
    --white: #ffffff;
    --paper-bottom: #e3f3fb;
    --photo-sky: #a9b8e2;
    --photo-haze: #c3c2d6;
    --photo-siding: #9a958f;
    --photo-glow: #d9b98a;
    --photo-ground: #5f5a48;
  }
  html, body {
    margin: 0;
    padding: 0;
    width: 1200px;
    height: 821px;
    overflow: hidden;
    background: var(--white);
  }
  .postcard {
    position: relative;
    width: 1200px;
    height: 821px;
    overflow: hidden;
    font-family: "Questrial", "Century Gothic", sans-serif;
  }
  .house-photo {
    position: absolute;
    inset: 0 0 120px 0;
    background:
      radial-gradient(ellipse 420px 200px at 560px 470px, rgba(236, 196, 130, 0.55), rgba(236, 196, 130, 0) 70%),
      linear-gradient(180deg, var(--photo-sky) 0%, var(--photo-haze) 30%, var(--photo-siding) 52%, var(--photo-glow) 72%, var(--photo-ground) 100%);
  }
  .waves {
    position: absolute;
    inset: 0;
    width: 1200px;
    height: 821px;
  }
  .brand {
    position: absolute;
    right: 44px;
    top: 50px;
    text-align: right;
    line-height: 1;
  }
  .brand-name {
    display: block;
    font-size: 48px;
    color: var(--navy);
    letter-spacing: 0.5px;
  }
  .brand-service {
    display: block;
    margin-top: 16px;
    font-size: 48px;
    color: var(--white);
    letter-spacing: 0.5px;
  }
  .brand-web {
    display: block;
    margin-top: 16px;
    font-size: 20px;
    color: var(--navy);
  }
  .services {
    position: absolute;
    left: 911px;
    top: 488px;
    width: 245px;
    height: 245px;
    border-radius: 50%;
    background: var(--sky-blue);
    color: var(--white);
    display: flex;
    flex-direction: column;
    justify-content: center;
    align-items: center;
    font-size: 27px;
    line-height: 35px;
    text-align: center;
  }
  .services p { margin: 0; }
  .offer {
    position: absolute;
    left: 0;
    width: 1172px;
    top: 719px;
    margin: 0;
    line-height: 30px;
    text-align: center;
    font-size: 24px;
    color: var(--navy);
  }
  .contact {
    position: absolute;
    left: 0;
    width: 1172px;
    top: 761px;
    height: 34px;
    display: flex;
    justify-content: center;
    align-items: center;
    gap: 16px;
    font-size: 23px;
    color: var(--navy);
  }
  .phone-icon { width: 34px; height: 34px; }
</style>
</head>
<body>
<main class="postcard">
  <div class="house-photo" role="img" aria-label="Photograph of a large two-storey shingled family home at dusk with lit windows, white garage doors and a landscaped front yard"></div>

  <svg class="waves" viewBox="0 0 1200 821" preserveAspectRatio="none" aria-hidden="true">
    <defs>
      <linearGradient id="paper" x1="0" y1="0" x2="0" y2="1">
        <stop offset="0" stop-color="#ffffff"/>
        <stop offset="1" stop-color="#e3f3fb"/>
      </linearGradient>
    </defs>
    <path d="M0,584 C200,640 380,664 560,664 C800,664 1000,628 1200,618 L1200,821 L0,821 Z" fill="#74cdf3"/>
    <path d="M0,520 C200,600 380,646 560,648 C800,650 1000,618 1200,606 L1200,622 C1000,634 800,666 560,666 C380,666 200,626 0,548 Z" fill="#1f4f9e"/>
    <path d="M0,650 C150,685 300,700 440,700 C700,700 950,662 1200,645 L1200,821 L0,821 Z" fill="url(#paper)"/>
  </svg>

  <header class="brand">
    <span class="brand-name">stoneridge</span>
    <span class="brand-service">power washing</span>
    <span class="brand-web">www.stoneridgepowerwashing.example</span>
  </header>

  <section class="services">
    <p>We Clean:</p>
    <p>Houses</p>
    <p>Decks</p>
    <p>Driveways</p>
    <p>Fences</p>
  </section>

  <p class="offer">Mention this card and receive a FREE standard size Deck Wash</p>

  <div class="contact">
    <span>Contact us today!</span>
    <svg class="phone-icon" viewBox="0 0 34 34" aria-hidden="true">
      <circle cx="17" cy="17" r="15" fill="none" stroke="#1d3f8c" stroke-width="2.5"/>
      <path d="M11.5,9.5 l3,-0.5 l2,4.5 l-2,1.6 c1,2.2 2.4,3.6 4.4,4.6 l1.6,-2 l4.5,2 l-0.5,3 c-6.5,0.8 -13.5,-6.2 -13,-13.2 z" fill="#1d3f8c"/>
    </svg>
    <span>804-555-3186</span>
  </div>
</main>
</body>
</html>
```